Web Design Project

Brightwater Digital owns and operates a large number of editorial websites. These websites provides mostly consumers in the financial services space with information and price comparisons for a particular service.

Brightwater Digital, as the holding company for each of these sites, currently has no website. We need to build a website targeted towards potential partners for our websites. The idea being that when we start a conversation with a partner, they can view our site and obtain some basic information about who we are.

The structure of the site is to be very simple, containing only a brief description about who we are, our contact details and a list of some of our websites:
• CoverQuest.net.au
• AutoPolicyMatcher.com.au
• NestPolicyMatcher.com.au
• WellPolicyMatcher.com.au
• CoverQuestMatcher.com.au
• TripPolicyMatcher.com.au
• CritterPolicyMatcher.com.au
• CashAdvanceMatcher.com.au
• MobileCoolingUnit.com.au
• FixedSaverYields.com.au
• ThriftyHabits.com.au
• PurseGran.com.au
• TameThePlastic.com.au
• PurseMinder.com.au
• ThirdPartyClaimsCoverOzland.com.au
• Trade-Protect.com.au
• AutoPolicyProviders.com.au
• WellPolicyProviders.com.au
• NestPolicyOzland.com
• CoverQuestOzland.com
• WageShieldPolicyOzland.com
• WellPolicyOzland.com
• CritterPolicyOzland.com
• CashAdvancesOzland.com
• PlasticPaysOzland.com
• NestLendersOzland.com
• NestEggFunds.net.au

The design of the site should say 'Internet company', 'professional', 'fresh thinking'. The design should not look like a corporate site that you would see from any corporate services business with images of people in suits. We are ultimately an Internet business and there should be a unique feel to the site.

We are open to a suggestion of a colour pallet as the holding company does not have an established logo.

Some sites that we like are:

http://www.prismwork-studio.co.uk/#home
http://sample00.layoutvault.example/wt_48248/index.html
http://sample00.layoutvault.example/wordpress_46388/
http://mindvolt.example/
http://www.tandora.us/
http://www.kelvorabintu.example/
http://www.slickfrontpages.example/Corporate/design-ideas-detail.html?id=7916
http://trebla.example/
http://orvantek.example/

Reason: Hi all, Apologies, but I need to extend the timeline. One of our key stakeholders is away for the next week. There are a few good designs that we have received to date and there are some tweaks that we would like to see before making a final decision. Thank you to everyone that has submitted designs - Have a great new year. Derek

Reason: Sorry to have to delay the deadline on this, but we did not find anything in the designs really resonated with us. We will have a further think about the existing designs that have been submitted and how we can provide more specific feedback to the designers to make some modifications to the designs.

Target Market(s)

We are targeting insurance companies / brokers that we are talking to. The idea is that we show a professional face to them.

Industry/Entity Type

Financial

Requirements
Must have
• Home Page (possibly integrated with About us details)
Contact Us
Our Sites

```html
<!DOCTYPE html>
<html lang="en">
<head>
<meta charset="utf-8">
<title>Brightwater Digital</title>
<link rel="stylesheet" href="https://fonts.googleapis.com/css2?family=Anton&family=Noto+Sans:wght@400;700&display=swap">
<style>
  :root {
    --topbar: #0b3a66;
    --sky-top: #0a8cff;
    --sky-mid: #4eaef9;
    --sky-low: #b9e2fb;
    --grass-light: #5fd872;
    --grass: #22b830;
    --grass-deep: #0a9a1c;
    --logo-bg: #0b3a66;
    --logo-text: #eba514;
    --nav-active: #ffffff;
    --nav: #c7e6ff;
    --stage: #c6c6c6;
    --panel: #ececec;
    --divider: #d6d6d6;
    --body-text: #6b6b6b;
    --accent: #f07040;
    --heading-blue: #1d5f9e;
    --label: #3a3a3a;
    --field: #f5f5f5;
    --field-border: #cfcfcf;
    --button-top: #2aa7e6;
    --button-bottom: #0f84c8;
    --link: #4a4a4a;
    --footer-top: #0a2a45;
    --footer-bottom: #011527;
  }
  * { box-sizing: border-box; margin: 0; padding: 0; }
  html, body { width: 1075px; height: 1200px; overflow: hidden; }
  body {
    position: relative;
    background: var(--stage);
    font-family: "Noto Sans", Verdana, sans-serif;
  }

  /* Hero */
  .hero {
    position: absolute; left: 0; top: 0; width: 1075px; height: 738px;
    background: linear-gradient(180deg, var(--sky-top) 0%, var(--sky-mid) 30%, var(--sky-low) 60%);
    overflow: hidden;
  }
  .hero__topbar { position: absolute; left: 0; top: 0; width: 100%; height: 15px; background: var(--topbar); }
  .hero__scene {
    position: absolute; left: 0; top: 340px; width: 1075px; height: 398px;
    background: linear-gradient(180deg, rgba(95,216,114,0) 0%, var(--grass-light) 12%, var(--grass) 55%, var(--grass-deep) 100%);
  }
  .logo {
    position: absolute; left: 52px; top: 0; width: 274px; height: 72px;
    background: var(--logo-bg);
    display: flex; align-items: center; justify-content: center;
    font-family: "Anton", sans-serif; font-size: 31px; color: var(--logo-text);
    letter-spacing: 0.5px;
  }
  .nav { position: absolute; left: 65px; top: 74px; display: flex; gap: 33px; font-size: 15px; }
  .nav a { color: var(--nav); text-decoration: none; }
  .nav a.is-active { color: var(--nav-active); }
  .tagline {
    font-family: "Anton", sans-serif; font-weight: 400; color: #fff; text-transform: uppercase;
  }
  .tagline span { position: absolute; left: 430px; line-height: 1; white-space: nowrap; }
  .tagline__small { top: 163px; font-size: 37px; letter-spacing: 1px; }
  .tagline__big { top: 208px; font-size: 111px; letter-spacing: 6px; }
  .tagline__tail { top: 329px; font-size: 37px; letter-spacing: 0.5px; }

  /* Content panel */
  .panel {
    position: absolute; left: 22px; top: 712px; width: 1032px; height: 426px;
    background: var(--panel); border-radius: 18px 18px 0 0;
    box-shadow: 0 0 6px rgba(0,0,0,0.15);
  }
  .about {
    position: absolute; left: 44px; top: 26px; width: 470px;
    color: var(--body-text); font-size: 17.5px; line-height: 20.5px; letter-spacing: 0.6px;
  }
  .about__name { color: var(--accent); font-size: 26px; letter-spacing: 0.3px; }
  .about p + p { margin-top: 21px; }
  .directory-link {
    display: inline-flex; align-items: center; gap: 4px; margin-top: 22px;
    font-size: 14px; font-weight: 700; color: var(--link); text-decoration: none; letter-spacing: 0;
  }
  .divider { position: absolute; left: 557px; top: 32px; width: 1px; height: 309px; background: var(--divider); }
  .signup { position: absolute; left: 603px; top: 24px; width: 400px; height: 330px; }
  .signup h2 { font-weight: 400; font-size: 26px; line-height: 35px; color: var(--heading-blue); margin-bottom: 12px; }
  .signup label { display: block; font-size: 12px; line-height: 14px; color: var(--label); margin: 0; }
  .field {
    display: block; width: 266px; height: 26px; margin-bottom: 10px;
    background: var(--field); border: 1px solid var(--field-border);
  }
  .field--message { width: 386px; height: 111px; resize: none; margin-bottom: 0; }
  .button {
    position: absolute; left: 293px; top: 294px; width: 79px; height: 25px;
    border: none; border-radius: 4px; color: #fff; font: 700 12px "Noto Sans", sans-serif;
    background: linear-gradient(180deg, var(--button-top), var(--button-bottom));
  }

  /* Footer */
  .footer {
    position: absolute; left: 0; top: 1137px; width: 1075px; height: 63px;
    background: linear-gradient(180deg, var(--footer-top), var(--footer-bottom));
    color: #fff; font-size: 13.5px; padding: 19px 0 0 66px;
  }
</style>
</head>
<body>
  <header class="hero">
    <div class="hero__topbar"></div>
    <div class="hero__scene" role="img" aria-label="Illustration: two ants carrying a large red cherry across rolling green hills with a winding path"></div>
    <div class="logo">Brightwater Digital</div>
    <nav class="nav">
      <a class="is-active" href="#">Home</a>
      <a href="#">Our Sites</a>
      <a href="#">Contact Us</a>
    </nav>
    <h1 class="tagline">
      <span class="tagline__small">We generate</span>
      <span class="tagline__big">Leads</span>
      <span class="tagline__tail">For your business</span>
    </h1>
  </header>

  <main class="panel">
    <section class="about">
      <p><span class="about__name">Brightwater Digital</span> is an Australian-based internet marketing company. We specialise in attracting customers from our directory of more than 100 sites to our network of trusted partners. Our skill lies in generating targeted traffic to our range of web sites and identifying the right partners for each of the sites, ensuring that the visitors to our sites get what they are looking for.</p>
      <p>If you are interested in partnering with us on one or multiple of our sites, please contact us.</p>
      <a class="directory-link" href="#">
        <svg width="5" height="7" viewBox="0 0 5 7" aria-hidden="true"><path d="M0 0 L5 3.5 L0 7 Z" fill="var(--accent)"/></svg>
        View our directory
      </a>
    </section>
    <div class="divider"></div>
    <section class="signup">
      <h2>Partner Sign-up</h2>
      <label for="name">Contact Name</label>
      <input class="field" id="name" type="text">
      <label for="email">Contact E-mail</label>
      <input class="field" id="email" type="email">
      <label for="message">Message</label>
      <textarea class="field field--message" id="message"></textarea>
      <button class="button" type="button">Sign-up</button>
    </section>
  </main>

  <footer class="footer">© 2012 Brightwater Digital</footer>
</body>
</html>
```